Stationery Design Project for Marketing Consultancy

I have started a new consultancy business and require the following elements to be designed using existing logo:
• Business card
• Letterhead
• Envelope (DL, C4, C5)
• Microsoft word template for report writing
• A4 Presentation Folder
• Powerpoint template
COPY FOR FRONT AND BACK OF BUSINESS CARD
logo
'Countable Growth. Bold Outcomes' slogan (but no need to use existing lockup with logo)
name, B Bus. Mktg, Grad Dip Digital Mktg, CPM (post nominal abbreviations in smaller font)
mobile: 04XX-XXX-XXX (I will give details to the winner to add)
website: www.quorvale.com.au
email: info@quorvale.com.au
COPY FOR LETTERHEAD
Logo
Company Name
Please, submit your designs that include business card, letterhead and envelope. Once selected the winner will be asked to complete the project by creating the rest of the artwork.
FINAL FILES
Print ready files to be supplied as well as Indesign files so that minor amends can be made if necessary in future.
• Layered vectors in EPS & PDF
• Screen quality JPEG & PNGs
ABOUT THE BUSINESS: QUORVALE
I work with clients to understand their business challenges, developing and executing measurable marketing strategies tied to key business metrics. Services include:
Services include:
• Business planning and business development
• Marketing and brand strategy
• Insight-driven integrated campaigns
• Loyalty programs and retention marketing
• Marketing automation
• Direct marketing (traditional and digital)
• Content strategy and development
Hi everyone,
Target Market(s)
Corporate decision makers (heads of marketing, general managers etc) and small to medium sized business owners. Predominately male aged 35+
Industry/Entity Type
Marketing
Requirements
Must have
- BRAND PERSONALITY
The successful design will communicate brand personality. I am a professional, results-driven entrepreneur, but want to show off my creative flair.
MEMORABILITY
Looking for a unique and eye-catching design. Am considering special printing effects (die cuts, letterpress, interactive elements, embossing, foiling etc) or a striking minimalist approach.
Nice to have
- I have a mission that could be incorporated on reverse if room -
Turning insights into actions & passion into profit.
Should not have
- Use of pink or green.

```html
<!DOCTYPE html>
<html lang="en">
<head>
<meta charset="utf-8">
<title>Quorvale Stationery</title>
<link rel="stylesheet" href="https://fonts.googleapis.com/css2?family=Montserrat:wght@700;800&family=Arimo:wght@400;700&display=swap">
<style>
  :root {
    --bg: #f1f1f2;
    --paper: #ffffff;
    --ink: #222528;
    --ink-soft: #55595d;
    --slate: #30363c;
    --slate-mark: #4b5259;
    --rule: #3a3e42;
  }
  * { box-sizing: border-box; margin: 0; padding: 0; }
  html, body { width: 1200px; height: 927px; overflow: hidden; }
  body { background: var(--bg); font-family: "Arimo", Arial, sans-serif; color: var(--ink); position: relative; }

  .sheet { position: absolute; background: var(--paper); border: 1px solid #e2e2e4; }
  .dark { background: var(--slate); border-color: var(--slate); }

  .logo { position: absolute; display: flex; flex-direction: column; align-items: center; }
  .logo-dot { border-radius: 50%; background: var(--ink); }
  .logo-name { font-family: "Montserrat", Arial, sans-serif; font-weight: 800; color: var(--ink); letter-spacing: .02em; line-height: 1; }
  .logo-tag { font-family: "Montserrat", Arial, sans-serif; font-weight: 700; color: var(--ink); text-transform: uppercase; line-height: 1; white-space: nowrap; }

  .logo.small .logo-dot { width: 22px; height: 22px; margin-bottom: 5px; }
  .logo.small .logo-name { font-size: 14px; }
  .logo.small .logo-tag { font-size: 3.6px; margin-top: 2px; letter-spacing: .02em; }

  /* Letterhead */
  .letterhead { left: 185px; top: 98px; width: 398px; height: 516px; }
  .letterhead .logo { left: 52px; top: 42px; }
  .letter-body { position: absolute; left: 45px; top: 153px; width: 315px; }
  .letter-heading { font-weight: 700; font-size: 7.4px; text-transform: uppercase; margin-bottom: 11px; }
  .letter-body p { font-size: 7px; line-height: 11px; margin-bottom: 11px; }
  .contact-row { position: absolute; display: flex; align-items: center; font-size: 6.6px; color: var(--ink); }
  .contact-item { display: flex; align-items: center; gap: 4px; }
  .contact-item svg { width: 8px; height: 8px; fill: var(--ink); }
  .letter-rule { position: absolute; left: 45px; top: 480px; width: 308px; height: 1px; background: var(--rule); }
  .letterhead .contact-row { left: 45px; top: 488px; width: 308px; justify-content: space-between; }

  /* Folder */
  .folder { left: 609px; top: 55px; width: 420px; height: 559px; overflow: hidden; }
  .folder-mark { position: absolute; left: 0; top: 0; width: 100%; text-align: center; top: 165px; display: flex; flex-direction: column; align-items: center; }
  .folder-mark .mark-dot { width: 96px; height: 96px; border-radius: 50%; background: var(--slate-mark); margin-bottom: 14px; }
  .folder-mark .logo-name { color: var(--slate-mark); font-size: 40px; }
  .folder-mark .logo-tag { color: var(--slate-mark); font-size: 10.5px; margin-top: 5px; font-weight: 700; letter-spacing: .01em; }

  /* Business card */
  .card-front { left: 45px; top: 639px; width: 123px; height: 202px; }
  .card-front .logo { left: 12px; top: 14px; }
  .card-front .logo.small .logo-dot { width: 20px; height: 20px; }
  .card-front .logo.small .logo-name { font-size: 13px; }
  .card-name { position: absolute; left: 0; width: 100%; top: 122px; text-align: center; font-family: "Montserrat", Arial, sans-serif; font-weight: 800; font-size: 9px; }
  .card-creds { position: absolute; left: 0; width: 100%; top: 134px; text-align: center; font-size: 3.6px; color: var(--ink-soft); }
  .card-contacts { position: absolute; left: 12px; top: 149px; display: flex; flex-direction: column; gap: 5px; font-size: 3.8px; }
  .card-contacts .contact-item svg { width: 6px; height: 6px; }
  .card-back { left: 185px; top: 639px; width: 110px; height: 202px; }
  .card-back .mark-dot { position: absolute; left: 35px; top: 80px; width: 40px; height: 40px; border-radius: 50%; background: var(--slate-mark); }

  /* Envelope front */
  .envelope-front { left: 321px; top: 639px; width: 408px; height: 202px; }
  .envelope-front .logo { left: 28px; top: 18px; }
  .envelope-front .contact-row { left: 42px; top: 182px; gap: 26px; }

  /* Envelope back */
  .envelope-back { left: 754px; top: 639px; width: 405px; height: 202px; }
  .envelope-back svg.flap { position: absolute; left: 0; top: 0; }
</style>
</head>
<body>

<section class="sheet letterhead" aria-label="Letterhead">
  <div class="logo small">
    <div class="logo-dot"></div>
    <div class="logo-name">QUORVALE</div>
    <div class="logo-tag">Countable Growth. Bold Outcomes</div>
  </div>
  <div class="letter-body">
    <h2 class="letter-heading">Duis aute irure dolor in reprehenderit in voluptate</h2>
    <p>Lorem ipsum dolor sit amet, consectetur adipiscing elit. Fusce lobortis magna dui, vel condimentum quam hendrerit ut. Fusce id felis odio. Donec id ante faucibus, malesuada justo quis, pellentesque justo. Suspendisse nisi leo, ornare in tempus sed, ornare congue orci. Mauris dui magna, placerat at sodales sit amet, accumsan et lacus. Sed consequat scelerisque orci, non vulputate est porta ac. Nulla et diam et lacus volutpat viverra et vulputate mi.</p>
    <p>Integer vestibulum quis purus nec pretium. Quisque rhoncus ipsum at nulla tristique aliquet porta ut nisl. Curabitur egestas vitae lorem vel facilisis. Ut ornare eros et est dignissim dapibus. Quisque ultrices neque ac mi euismod, eget ultricies neque eleifend. Integer et leo feugiat lectus rhoncus faucibus et nec mi. Sed tincidunt elit sit amet scelerisque pretium.</p>
    <p>Vivamus enim urna, egestas eget lacus ut, pharetra rhoncus ipsum. Duis ut metus commodo, rhoncus odio vitae, consequat odio. Nam lectus est, ultricies vitae egestas vitae, suscipit non orci. Cum sociis natoque penatibus et magnis dis parturient montes, nascetur ridiculus mus.</p>
  </div>
  <div class="letter-rule"></div>
  <div class="contact-row">
    <span class="contact-item"><svg viewBox="0 0 10 10"><path d="M2 0.5 L3.6 0.5 L4.3 3 L3.1 3.9 Q4.2 6 6.1 6.9 L7 5.7 L9.5 6.4 L9.5 8 Q9.5 9.5 8 9.5 Q0.5 9 0.5 2 Q0.5 0.5 2 0.5Z"/></svg>04XX-XXX-XXX</span>
    <span class="contact-item"><svg viewBox="0 0 10 10"><circle cx="5" cy="5" r="4.3" fill="none" stroke="#222528" stroke-width="1"/><path d="M0.7 5H9.3M5 0.7Q2.4 5 5 9.3M5 0.7Q7.6 5 5 9.3" fill="none" stroke="#222528" stroke-width=".8"/></svg>www.quorvale.com.au</span>
    <span class="contact-item"><svg viewBox="0 0 10 10"><rect x="0.5" y="2" width="9" height="6.5"/><path d="M0.5 2L5 5.8L9.5 2" fill="none" stroke="#fff" stroke-width=".8"/></svg>info@quorvale.com.au</span>
  </div>
</section>

<section class="sheet dark folder" role="img" aria-label="Presentation folder in dark slate linen texture with faint brand mark">
  <div class="folder-mark">
    <div class="mark-dot"></div>
    <div class="logo-name">QUORVALE</div>
    <div class="logo-tag">Countable Growth. Bold Outcomes</div>
  </div>
</section>

<section class="sheet card-front" aria-label="Business card front">
  <div class="logo small">
    <div class="logo-dot"></div>
    <div class="logo-name">QUORVALE</div>
    <div class="logo-tag">Countable Growth. Bold Outcomes</div>
  </div>
  <div class="card-name">SAM CARTER</div>
  <div class="card-creds">B Bus. Mktg, Grad Dip Digital Mktg, CPM</div>
  <div class="card-contacts">
    <span class="contact-item"><svg viewBox="0 0 10 10"><path d="M2 0.5 L3.6 0.5 L4.3 3 L3.1 3.9 Q4.2 6 6.1 6.9 L7 5.7 L9.5 6.4 L9.5 8 Q9.5 9.5 8 9.5 Q0.5 9 0.5 2 Q0.5 0.5 2 0.5Z"/></svg>04XX-XXX-XXX</span>
    <span class="contact-item"><svg viewBox="0 0 10 10"><circle cx="5" cy="5" r="4.5"/></svg>www.quorvale.com.au</span>
    <span class="contact-item"><svg viewBox="0 0 10 10"><rect x="0.5" y="2" width="9" height="6.5"/></svg>info@quorvale.com.au</span>
  </div>
</section>

<section class="sheet dark card-back" role="img" aria-label="Business card back in dark slate linen texture with faint brand mark">
  <div class="mark-dot"></div>
</section>

<section class="sheet envelope-front" aria-label="DL envelope front">
  <div class="logo small">
    <div class="logo-dot"></div>
    <div class="logo-name">QUORVALE</div>
    <div class="logo-tag">Countable Growth. Bold Outcomes</div>
  </div>
  <div class="contact-row">
    <span class="contact-item"><svg viewBox="0 0 10 10"><path d="M2 0.5 L3.6 0.5 L4.3 3 L3.1 3.9 Q4.2 6 6.1 6.9 L7 5.7 L9.5 6.4 L9.5 8 Q9.5 9.5 8 9.5 Q0.5 9 0.5 2 Q0.5 0.5 2 0.5Z"/></svg>04XX-XXX-XXX</span>
    <span class="contact-item"><svg viewBox="0 0 10 10"><circle cx="5" cy="5" r="4.3" fill="none" stroke="#222528" stroke-width="1"/><path d="M0.7 5H9.3M5 0.7Q2.4 5 5 9.3M5 0.7Q7.6 5 5 9.3" fill="none" stroke="#222528" stroke-width=".8"/></svg>www.quorvale.com.au</span>
    <span class="contact-item"><svg viewBox="0 0 10 10"><rect x="0.5" y="2" width="9" height="6.5"/><path d="M0.5 2L5 5.8L9.5 2" fill="none" stroke="#fff" stroke-width=".8"/></svg>info@quorvale.com.au</span>
  </div>
</section>

<section class="sheet envelope-back" aria-label="DL envelope back">
  <svg class="flap" width="405" height="100" viewBox="0 0 405 100" role="img" aria-label="Envelope flap in dark slate linen texture with faint brand mark">
    <path d="M0 0H405V16Q402 30 382 38L226 88Q203 96 180 88L23 38Q3 30 0 16Z" fill="#30363c"/>
    <circle cx="203" cy="28" r="14" fill="#4b5259"/>
  </svg>
</section>

</body>
</html>
```